brightwave pools cards

i need to create a design to use on my business cards,brochures and as a letterhead. i am a new swimming pool renovation business named BRIGHTWAVE POOLS. I require a smart professional deign to reflect that my business is the best in the industry.
should include something like.... Brightwave Pools ABN - 57184620931
residential pool renovation specialists
specialising in the art of - fully tiled pools
- waterline tiles
- natural stone pool copings
and outdoor areas - concrete slabs - detailed mosaic work - pool lighting and water features - pool painting

trent - 0461829304 gordon -0438152967 brightwavepoolsnorth@mailbox-example.com

the design could feature - water, natural stone (travertine, sandstone etc), something to personafy the word imagine.
looking foward to seeing some ideas... cheers heaps trent

```html
<!DOCTYPE html>
<html lang="en">
<head>
<meta charset="utf-8">
<title>Brightwave Pools – Business Cards</title>
<link rel="stylesheet" href="https://fonts.googleapis.com/css2?family=Exo+2:wght@300;400;600&display=swap">
<style>
  :root {
    --pool-blue: #2387c9;
    --pool-blue-deep: #1a6fa8;
    --ink: #3a3f45;
    --ink-soft: #6b7178;
    --paper: #ffffff;
    --backdrop: #e9ecef;
  }
  * { box-sizing: border-box; margin: 0; padding: 0; }
  html, body {
    width: 1200px; height: 900px; overflow: hidden;
    background: var(--backdrop);
    font-family: "Exo 2", sans-serif;
  }
  .sheet {
    position: relative; width: 1200px; height: 900px;
    display: flex; flex-direction: column; align-items: center; justify-content: center; gap: 40px;
  }
  .card {
    position: relative; width: 700px; height: 400px; overflow: hidden;
    box-shadow: 0 6px 18px rgba(0,0,0,.18);
  }

  /* Front */
  .card--front { background: var(--pool-blue); color: var(--paper); }
  .front__brand {
    position: absolute; left: 60px; top: 130px; width: 300px; text-align: right;
  }
  .wordmark { font-weight: 600; font-size: 46px; line-height: 1; letter-spacing: -0.5px; }
  .front__abn { margin-top: 10px; font-size: 17px; color: var(--ink); letter-spacing: 1px; font-weight: 400; }
  .front__divider {
    position: absolute; left: 385px; top: 122px; width: 2px; height: 100px; background: var(--paper); opacity: .85;
  }
  .front__tagline {
    position: absolute; left: 410px; top: 140px; font-weight: 300; font-size: 27px; line-height: 1.2;
  }

  /* Back */
  .card--back { background: var(--paper); color: var(--ink); }
  .back__brand { position: absolute; right: 50px; top: 40px; text-align: right; }
  .back__brand .wordmark { color: var(--pool-blue); font-size: 34px; }
  .back__abn { margin-top: 6px; font-size: 13px; color: var(--ink-soft); letter-spacing: 1px; }
  .contacts { position: absolute; left: 50px; top: 70px; display: flex; gap: 16px; align-items: flex-start; }
  .contacts__icon {
    width: 38px; height: 38px; border-radius: 8px; background: var(--ink);
    display: flex; align-items: center; justify-content: center;
  }
  .contacts__list { list-style: none; font-size: 19px; line-height: 1.5; }
  .contacts__list .name { font-weight: 600; }
  .email { position: absolute; left: 104px; top: 160px; font-size: 17px; color: var(--ink-soft); }
  .services {
    position: absolute; left: 0; right: 0; bottom: 0; height: 150px;
    background: var(--pool-blue); color: var(--paper); padding: 22px 50px;
  }
  .services__title { font-size: 15px; font-weight: 600; letter-spacing: 1px; text-transform: uppercase; opacity: .9; }
  .services__list {
    list-style: none; margin-top: 10px; columns: 2; column-gap: 40px; font-size: 17px; font-weight: 300; line-height: 1.45;
  }
</style>
</head>
<body>
<main class="sheet">

  <section class="card card--front" aria-label="Business card front">
    <div class="front__brand">
      <div class="wordmark">Brightwave Pools</div>
      <div class="front__abn">ABN - 57184620931</div>
    </div>
    <div class="front__divider"></div>
    <p class="front__tagline">Residential pool<br>renovation specialists</p>
  </section>

  <section class="card card--back" aria-label="Business card back">
    <div class="back__brand">
      <div class="wordmark">Brightwave Pools</div>
      <div class="back__abn">ABN - 57184620931</div>
    </div>

    <div class="contacts">
      <span class="contacts__icon">
        <svg width="22" height="22" viewBox="0 0 24 24" aria-hidden="true">
          <path fill="#ffffff" d="M6.6 10.8a15.1 15.1 0 0 0 6.6 6.6l2.2-2.2a1 1 0 0 1 1-.25 11.4 11.4 0 0 0 3.6.57 1 1 0 0 1 1 1V20a1 1 0 0 1-1 1A17 17 0 0 1 3 4a1 1 0 0 1 1-1h3.5a1 1 0 0 1 1 1c0 1.25.2 2.45.57 3.57a1 1 0 0 1-.25 1z"/>
        </svg>
      </span>
      <ul class="contacts__list">
        <li><span class="name">Trent</span> - 0461829304</li>
        <li><span class="name">Gordon</span> - 0438152967</li>
      </ul>
    </div>
    <p class="email">brightwavepoolsnorth@mailbox-example.com</p>

    <div class="services">
      <p class="services__title">Specialising in</p>
      <ul class="services__list">
        <li>Fully tiled pools</li>
        <li>Waterline tiles</li>
        <li>Natural stone pool copings</li>
        <li>Pool lighting</li>
      </ul>
    </div>
  </section>

</main>
</body>
</html>
```